Simple Website Design for Law Office

I need a website design for our law office (Law Offices of Marcus Trell) that is extremely simple, only including a landing page and perhaps a contact page (parallax scrolling).

Website should look similar to this one (template): https://www.quorvelbaxon.com/

Design should be modern, simple, and inviting. There are a few assets like logo, stock photos/icons we would like added as well, and some language and contact info, but very basic stuff.

The name of the company is: Law Offices of Marcus Trell

Target Market(s)

B2B corporate clients, users from Canada, UK, East Asia, and all potential users with immigration needs

Coding

Coded - Design and coding required

Number of Pages Required

2 page

Colors

Designer to choose colors to be used in the design.

Requirements
Must have
• Landing page, Contact Page
• Simple, elegant design with minimalist font
Nice to have
• Parallax scrolling, so one page and can scroll to contact us segment

```html
<!DOCTYPE html>
<html lang="en">
<head>
<meta charset="utf-8">
<title>Law Offices of Marcus Trell</title>
<link href="https://fonts.googleapis.com/css2?family=Noto+Serif:wght@400;700&family=Open+Sans:wght@400;600;700&display=swap" rel="stylesheet">
<style>
:root{
  --brand:#4b3fc6;
  --brand-dark:#3a2fae;
  --ink:#222230;
  --muted:#555862;
  --panel:#ececee;
  --white:#ffffff;
  --hero-dark:#2a2c3a;
  --twitter:#1da1f2;
  --pink:#e4246e;
}
*{box-sizing:border-box;margin:0;padding:0}
html,body{width:1200px;height:2568px;overflow:hidden}
body{position:relative;background:var(--white);font-family:"Open Sans",Arial,sans-serif;color:var(--ink)}
.topbar{position:absolute;left:0;top:0;width:1200px;height:32px;background:var(--brand);color:var(--white);font-size:11px;display:flex;align-items:center;padding:0 150px;gap:0}
.topbar .address{flex:1;display:flex;align-items:center;gap:6px}
.topbar .email{display:flex;align-items:center;gap:6px;margin-right:40px}
.topbar .phone{font-size:17px;font-weight:600;display:flex;align-items:center;gap:8px}
.mainnav{position:absolute;top:32px;left:0;width:1200px;height:48px;background:var(--white);display:flex;justify-content:center;align-items:center;gap:28px;font-size:11px;font-weight:600;letter-spacing:.5px}
.mainnav a{color:var(--ink);text-decoration:none;padding:6px 0}
.mainnav a.active{color:var(--brand);border-bottom:2px solid var(--brand)}
.hero{position:absolute;top:80px;left:0;width:1200px;height:780px;overflow:hidden}
.hero-photo{position:absolute;inset:0;background:linear-gradient(180deg,#4a4d60 0%,#33364a 45%,#25273a 100%)}
.portrait{position:absolute;left:522px;top:240px;width:156px;height:156px;border-radius:50%;border:5px solid var(--white);background:linear-gradient(160deg,#c9c6c2,#8d8a8a)}
.hero h1{position:absolute;top:528px;width:100%;text-align:center;font-family:"Noto Serif",Georgia,serif;font-weight:400;font-size:40px;color:var(--white)}
.hero .cta{position:absolute;left:470px;top:594px;width:260px;height:44px;border-radius:22px;background:var(--brand);color:var(--white);font-family:"Noto Serif",Georgia,serif;font-style:italic;font-size:15px;display:flex;align-items:center;justify-content:center}
.hero .arrows{position:absolute;top:664px;width:100%;text-align:center;color:var(--white);font-size:24px;letter-spacing:14px}
.hero .slant{position:absolute;left:0;bottom:0}
.social{position:absolute;right:0;top:208px;width:40px}
.social span{display:block;width:40px;height:40px;margin-bottom:2px}
.social .s1{background:#1769c4}.social .s2{background:var(--twitter)}.social .s3{background:var(--pink)}
.welcome{position:absolute;top:980px;left:0;width:1200px;text-align:center}
.welcome h2{font-family:"Noto Serif",Georgia,serif;font-weight:400;font-size:38px;color:var(--ink)}
.welcome .role{margin-top:26px;font-weight:700;font-size:16px}
.welcome p{width:600px;margin:14px auto 0;font-size:13px;line-height:1.55;color:var(--muted)}
.btn{display:inline-block;background:var(--brand);color:var(--white);font-weight:700;font-size:13px;letter-spacing:.5px;border-radius:24px;padding:14px 40px;margin-top:38px}
.success{position:absolute;top:1258px;left:0;width:1200px}
.success h2{text-align:center;font-family:"Noto Serif",Georgia,serif;font-weight:400;font-size:32px}
.success .rule{width:60px;height:3px;background:var(--brand);margin:12px auto 0}
.cards{position:absolute;top:82px;left:140px;display:flex;gap:12px}
.card{width:300px;height:420px;background:var(--panel)}
.card .photo{height:160px;background:linear-gradient(135deg,#6d6a6a,#2e2d33)}
.card.featured .photo{background:linear-gradient(135deg,#c9c6c0,#5d6a78)}
.card .body{padding:34px 28px 0;text-align:center}
.card h3{font-size:15px;font-weight:700;letter-spacing:.5px;color:var(--ink);line-height:1.3}
.card p{margin-top:14px;font-size:11px;line-height:1.6;color:var(--muted)}
.card.featured .body{background:var(--brand);height:260px}
.card.featured h3,.card.featured p{color:var(--white)}
.office{position:absolute;top:1860px;left:0;width:1200px;height:480px;background:linear-gradient(135deg,#3a3b45 0%,#1f2028 60%,#2a2b33 100%)}
.office .info{position:absolute;left:175px;top:100px;color:var(--white)}
.office h2{font-family:"Noto Serif",Georgia,serif;font-weight:400;font-size:34px}
.office ul{list-style:none;margin-top:20px;font-size:12px;line-height:1.5}
.office li{display:flex;gap:10px;margin-bottom:12px}
.office li svg{flex:none;margin-top:2px}
.office .dots{display:flex;gap:10px;margin-top:8px}
.office .dots span{width:18px;height:18px;border-radius:50%;background:var(--white)}
.map{position:absolute;left:500px;top:80px;width:560px;height:360px;background:linear-gradient(160deg,#eef0ea,#dfe6d8)}
.footer-nav{position:absolute;top:2428px;width:1200px;display:flex;justify-content:center;gap:32px;font-size:11px;font-weight:600}
.footer-nav a{color:var(--ink);text-decoration:none}
.footer-nav a.active{color:var(--brand)}
.copyright{position:absolute;top:2482px;width:1200px;text-align:center;font-size:11px;color:var(--muted)}
.chat{position:absolute;left:952px;top:2512px;width:170px;height:44px;background:var(--brand);color:var(--white);border-radius:8px 8px 0 0;display:flex;align-items:center;justify-content:center;gap:8px;font-size:13px;font-weight:700}
</style>
</head>
<body>
<header class="topbar">
  <div class="address">
    <svg width="10" height="13" viewBox="0 0 10 13"><path d="M5 0a5 5 0 0 0-5 5c0 4 5 8 5 8s5-4 5-8a5 5 0 0 0-5-5z" fill="#fff"/><circle cx="5" cy="5" r="2" fill="#4b3fc6"/></svg>
    Law Offices of Marcus Trell | 4820 Halvern Ave, 4th Floor | Pell Rivers, CA 90014
  </div>
  <div class="email">
    <svg width="13" height="9" viewBox="0 0 13 9"><rect x=".5" y=".5" width="12" height="8" fill="none" stroke="#fff"/><path d="M.5 .5l6 4.5 6-4.5" fill="none" stroke="#fff"/></svg>
    mtrellfirm@mail.com
  </div>
  <div class="phone">
    <svg width="13" height="13" viewBox="0 0 24 24"><path d="M6.6 10.8a15 15 0 0 0 6.6 6.6l2.2-2.2a1 1 0 0 1 1-.25 11.4 11.4 0 0 0 3.6.57 1 1 0 0 1 1 1V20a1 1 0 0 1-1 1A17 17 0 0 1 3 4a1 1 0 0 1 1-1h3.5a1 1 0 0 1 1 1c0 1.25.2 2.45.57 3.57a1 1 0 0 1-.25 1z" fill="#fff"/></svg>
    (213) 555-0142
  </div>
</header>

<nav class="mainnav">
  <a class="active" href="#">HOME</a><a href="#">ABOUT US</a><a href="#">OUR SUCCESS</a><a href="#">CONTACT</a>
</nav>

<section class="hero">
  <div class="hero-photo" role="img" aria-label="Aerial view of downtown city towers"></div>
  <div class="portrait" role="img" aria-label="Portrait of the attorney"></div>
  <h1>Law Offices of Marcus Trell</h1>
  <div class="cta">Contact Us for a Consultation</div>
  <div class="arrows">‹ ›</div>
  <svg class="slant" width="1200" height="90" viewBox="0 0 1200 90"><polygon points="0,90 0,60 1200,0 1200,90" fill="#fff"/><polygon points="0,60 1200,0 1200,12 0,72" fill="#9a9cab" opacity=".5"/></svg>
</section>

<aside class="social"><span class="s1"></span><span class="s2"></span><span class="s3"></span></aside>

<section class="welcome">
  <h2>Welcome To Law Offices of Marcus Trell.</h2>
  <div class="role">Marcus Trell | Jun 2013 – Present</div>
  <p>Handle all clients needs including criminal, transactional, and general civil litigation: personal injury, wrongful foreclosure/loan modification, breach of contract.</p>
  <span class="btn">READ MORE</span>
</section>

<section class="success">
  <h2>OUR SUCCESS</h2>
  <div class="rule"></div>
  <div class="cards">
    <article class="card">
      <div class="photo" role="img" aria-label="Signing of loan documents"></div>
      <div class="body"><h3>FORECLOSURE / HBOR</h3>
        <p>A $1,000,000 settlement for a borrower in a wrongful foreclosure, wrongful eviction and loan modification case, resolved after two years of litigation and trial.</p></div>
    </article>
    <article class="card featured">
      <div class="photo" role="img" aria-label="Client reviewing an insurance claim"></div>
      <div class="body"><h3>PERSONAL INJURY / INSURANCE</h3>
        <p>$150,000 for damage to a commercial property after owner's fraudulent insurance coverage under client's policy.</p></div>
    </article>
    <article class="card">
      <div class="photo" role="img" aria-label="Hands in handcuffs"></div>
      <div class="body"><h3>CRIMINAL</h3>
        <p>Domestic violence charges dismissed prior to jury selection. Drug sales charges reduced to drug court and simple possession.</p></div>
    </article>
  </div>
</section>

<section class="office" role="img" aria-label="Dark city skyline backdrop">
  <div class="info">
    <h2>OUR OFFICE</h2>
    <ul>
      <li><svg width="10" height="13" viewBox="0 0 10 13"><path d="M5 0a5 5 0 0 0-5 5c0 4 5 8 5 8s5-4 5-8a5 5 0 0 0-5-5z" fill="#fff"/></svg><span>Law Offices of Marcus Trell<br>4820 Halvern Ave, 4th Floor<br>Pell Rivers, CA 90014</span></li>
      <li><svg width="12" height="12" viewBox="0 0 24 24"><path d="M6.6 10.8a15 15 0 0 0 6.6 6.6l2.2-2.2a1 1 0 0 1 1-.25 11.4 11.4 0 0 0 3.6.57 1 1 0 0 1 1 1V20a1 1 0 0 1-1 1A17 17 0 0 1 3 4a1 1 0 0 1 1-1h3.5a1 1 0 0 1 1 1c0 1.25.2 2.45.57 3.57a1 1 0 0 1-.25 1z" fill="#fff"/></svg><span>(213) 555-0142</span></li>
      <li><svg width="12" height="12" viewBox="0 0 12 12"><rect x="1" y="3" width="10" height="7" fill="#fff"/></svg><span>(213) 555-0143</span></li>
      <li><svg width="13" height="9" viewBox="0 0 13 9"><rect x=".5" y=".5" width="12" height="8" fill="none" stroke="#fff"/><path d="M.5 .5l6 4.5 6-4.5" fill="none" stroke="#fff"/></svg><span>mtrellfirm@mail.com</span></li>
    </ul>
    <div class="dots"><span></span><span></span></div>
  </div>
  <div class="map" role="img" aria-label="Street map showing the office location"></div>
</section>

<nav class="footer-nav">
  <a class="active" href="#">HOME</a><a href="#">ABOUT US</a><a href="#">OUR SUCCESS</a><a href="#">CONTACT</a>
</nav>
<div class="copyright">© 2019 &nbsp;|&nbsp; www.marcustrelllaw.com</div>
<div class="chat">
  <svg width="16" height="14" viewBox="0 0 16 14"><path d="M1 1h14v9H6l-4 3v-3H1z" fill="#fff"/></svg>
  CHAT NOW
</div>
</body>
</html>
```